Business Card design for construction company

I would like a business card design for a construction company - Harlow Constructions. I have attached the ai logo file for use. I would like the card to be very smart and clean and incorporate only white and the two colours in the logo. I would like the card to have two sides. One side can just have the logo, the other with the relevant information.

Target Market(s)

Building and Construction Clients

Industry/Entity Type

Business

Contact Information for Business Card

Name: Tom Pardoe
Company: Harlow Constructions Pty Limited
Address: 14 Mallee Crescent Carrow Vale 2093
Phone: 0427 531 068
Email: tomp@harlowbuild-example.com.au

Font styles to use
Serif
Sans Serif

Requirements
Must have
• Details noted above
• Logo as provided
• Colours as in logo
• Square edges
• A font that compliments the logo
Should not have
• Any colour other than white and those in logo
• Rounded edges

```html
<!DOCTYPE html>
<html lang="en">
<head>
<meta charset="utf-8">
<title>Harlow Constructions — Business Card</title>
<link rel="stylesheet" href="https://fonts.googleapis.com/css2?family=Lato:wght@400;700&display=swap">
<style>
  :root {
    --brand-blue: #00a9ec;
    --brand-grey: #545456;
    --card-white: #ffffff;
    --stage: #ececec;
  }
  * { margin: 0; padding: 0; box-sizing: border-box; }
  html, body { width: 1200px; height: 900px; overflow: hidden; }
  body {
    position: relative;
    background: var(--stage);
    font-family: "Lato", Arial, sans-serif;
  }
  .card {
    position: absolute;
    overflow: hidden;
    box-shadow: 0 6px 18px rgba(0,0,0,0.18);
  }
  .card--details {
    left: 177px; top: 73px;
    width: 590px; height: 365px;
    background: var(--card-white);
  }
  .card--logo {
    left: 388px; top: 505px;
    width: 567px; height: 352px;
    background: var(--brand-blue);
  }
  .card__bands { position: absolute; inset: 0; }
  .wordmark {
    position: absolute;
    left: 0; right: 0;
    display: flex; align-items: center; justify-content: center;
    gap: 12px;
    font-weight: 400;
    letter-spacing: 3px;
    text-transform: uppercase;
    white-space: nowrap;
  }
  .wordmark__square { width: 14px; height: 14px; }
  .card--details .wordmark {
    top: 80px; font-size: 24px; color: var(--brand-grey);
  }
  .card--details .wordmark__square { background: var(--brand-blue); }
  .card--logo .wordmark {
    top: 160px; font-size: 26px; color: var(--card-white);
  }
  .card--logo .wordmark__square { background: var(--card-white); }

  .contact {
    position: absolute;
    left: 30px; top: 240px;
    color: var(--card-white);
    font-size: 16.5px;
    line-height: 22px;
  }
  .contact__row { display: flex; align-items: center; gap: 5px; }
  .contact__icon { width: 13px; height: 13px; fill: var(--brand-blue); }
  .contact__address { margin-top: 9px; }
  .holder-name {
    position: absolute;
    right: 38px; top: 262px;
    color: var(--brand-blue);
    font-weight: 700;
    font-size: 22px;
    letter-spacing: 0.5px;
    text-transform: uppercase;
  }
</style>
</head>
<body>

  <section class="card card--details" aria-label="Business card, details side">
    <svg class="card__bands" width="590" height="365" viewBox="0 0 590 365" aria-hidden="true">
      <polygon points="0,190 392,190 372,212 0,212" fill="var(--brand-blue)"/>
      <polygon points="0,217 376,217 406,182 590,182 590,365 0,365" fill="var(--brand-grey)"/>
    </svg>

    <div class="wordmark">
      <span class="wordmark__square"></span>
      <span>Harlow Constructions</span>
    </div>

    <div class="contact">
      <div class="contact__row">
        <svg class="contact__icon" viewBox="0 0 16 16" aria-hidden="true"><path d="M3.5 1h2.5l1.2 3.2-1.7 1.2a8.5 8.5 0 0 0 5.1 5.1l1.2-1.7L15 10v2.5c0 1-0.8 1.5-1.5 1.5A12.5 12.5 0 0 1 2 2.5C2 1.8 2.5 1 3.5 1z"/></svg>
        <span>0427 531 068</span>
      </div>
      <div class="contact__row">
        <svg class="contact__icon" viewBox="0 0 16 16" aria-hidden="true"><path d="M1 3h14v10H1z M1.5 3.5 8 9l6.5-5.5" fill="var(--brand-blue)"/><path d="M1.5 3.8 8 9l6.5-5.2" fill="none" stroke="var(--brand-grey)" stroke-width="1.2"/></svg>
        <span>tomp@harlowbuild-example.com.au</span>
      </div>
      <div class="contact__address">
        <div>Harlow Constructions Pty Limited</div>
        <div>14 Mallee Crescent Carrow Vale 2093</div>
      </div>
    </div>

    <div class="holder-name">Tom Pardoe</div>
  </section>

  <section class="card card--logo" aria-label="Business card, logo side">
    <div class="wordmark">
      <span class="wordmark__square"></span>
      <span>Harlow Constructions</span>
    </div>
  </section>

</body>
</html>
```